Business card design for IT consulting company

Looking for a simple, modern, clean business card design.
Open to reworking our existing logo.

Attached is our current business cards which we do not like.
Ideally double sided with something simple on the back.
Rectangle / Horizonal only.
No rounded edges on the card.
White as the dominate color is preferred.

Target Market(s)

clients, legal, oil & gas, medical, professionals

Industry/Entity Type

IT, tech, consulting

Contact Information for Business Card

Name, Title, email, phone, cell, website

Font styles to use
Sans Serif

Requirements
Must have
• Clean design
Should not have
• loud colors or unusual fonts, etc

```html
<!DOCTYPE html>
<html lang="en">
<head>
<meta charset="utf-8">
<title>Kelvo Solutions — Business Card</title>
<link rel="stylesheet" href="https://fonts.googleapis.com/css2?family=Montserrat:wght@500;700&display=swap">
<style>
  :root {
    --bg: #9a9a9a;
    --card-white: #ffffff;
    --card-black: #111111;
    --ink: #161616;
    --navy: #262673;
    --grey-text: #555555;
    --yellow: #fdc833;
    --red: #ee4156;
    --blue: #4bb2e3;
  }
  * { margin: 0; padding: 0; box-sizing: border-box; }
  html, body { width: 1200px; height: 588px; overflow: hidden; }
  body {
    background: var(--bg);
    font-family: "Montserrat", Arial, sans-serif;
    position: relative;
  }
  .card {
    position: absolute;
    top: 142px;
    width: 486px;
    height: 287px;
  }
  .card-back { left: 87px; background: var(--card-black); }
  .card-front { left: 622px; background: var(--card-white); }

  .back-brand {
    position: absolute; inset: 0;
    display: flex; align-items: center; justify-content: center; gap: 12px;
    color: #ffffff; font-weight: 700; font-size: 30px; letter-spacing: -0.5px;
  }
  .back-brand .brand-square { width: 34px; height: 34px; background: var(--yellow); }

  .front-brand {
    position: absolute; left: 48px; top: 126px;
    display: flex; align-items: center; gap: 8px;
    color: var(--ink); font-weight: 700; font-size: 21px; letter-spacing: -0.5px;
    white-space: nowrap;
  }
  .front-brand .brand-square { width: 32px; height: 32px; background: var(--navy); flex: none; }

  .divider {
    position: absolute; left: 281px; top: 86px;
    width: 2px; height: 115px; background: var(--navy);
  }
  .contact { position: absolute; left: 304px; top: 81px; }
  .contact-name {
    font-weight: 700; font-size: 18px; color: var(--navy); letter-spacing: 0.2px; line-height: 22px;
  }
  .contact-title {
    font-weight: 500; font-size: 13px; color: var(--grey-text); line-height: 18px; margin-bottom: 10px;
  }
  .contact-list { list-style: none; }
  .contact-list li {
    display: flex; align-items: center; gap: 7px;
    font-weight: 500; font-size: 13px; color: var(--grey-text); line-height: 18.4px;
    white-space: nowrap;
  }
  .contact-list svg { width: 10px; height: 10px; flex: none; }

  .color-bar {
    position: absolute; left: 0; bottom: 0; width: 100%; height: 12px; display: flex;
  }
  .color-bar span { flex: 1; }
  .bar-yellow { background: var(--yellow); }
  .bar-red { background: var(--red); }
  .bar-blue { background: var(--blue); }
  .bar-navy { background: var(--navy); }
</style>
</head>
<body>
  <section class="card card-back">
    <div class="back-brand"><span class="brand-square"></span>Kelvo Solutions</div>
  </section>

  <section class="card card-front">
    <div class="front-brand"><span class="brand-square"></span>Kelvo Solutions</div>
    <div class="divider"></div>
    <div class="contact">
      <p class="contact-name">DANIEL REYES</p>
      <p class="contact-title">IT Consultant</p>
      <ul class="contact-list">
        <li>
          <svg viewBox="0 0 10 10"><path d="M2 0.5 L3.6 2.6 L2.7 3.6 Q3.6 5.8 6.2 7.2 L7.3 6.3 L9.5 8 L8.3 9.5 Q2.5 9 0.5 2 Z" fill="var(--yellow)"/></svg>
          (888) 555-0148
        </li>
        <li>
          <svg viewBox="0 0 10 10"><rect x="2.5" y="0.5" width="5" height="9" rx="0.8" fill="none" stroke="var(--red)" stroke-width="1.2"/><circle cx="5" cy="7.8" r="0.6" fill="var(--red)"/></svg>
          (604) 555-0193
        </li>
        <li>
          <svg viewBox="0 0 10 10"><rect x="0.5" y="2" width="9" height="6.5" fill="var(--blue)"/><path d="M0.5 2 L5 5.5 L9.5 2" fill="none" stroke="#fff" stroke-width="0.9"/></svg>
          daniel.reyes@kelvo.ca
        </li>
        <li>
          <svg viewBox="0 0 10 10"><circle cx="5" cy="5" r="4.5" fill="var(--navy)"/><path d="M0.5 5 H9.5 M5 0.5 Q2.5 5 5 9.5 M5 0.5 Q7.5 5 5 9.5" fill="none" stroke="#fff" stroke-width="0.7"/></svg>
          www.kelvo.ca
        </li>
      </ul>
    </div>
    <div class="color-bar">
      <span class="bar-yellow"></span><span class="bar-red"></span><span class="bar-blue"></span><span class="bar-navy"></span>
    </div>
  </section>
</body>
</html>
```